Einfache Webside für kleine Promotion- und Personalagentur
Zielgruppe
Lumo Staffing ist eine international tätige Promotion- und Personalagentur. Wir bieten auch im Bereich Sport der jew. Sportart affine Hostessen und Hosts f an.
Aufgabenstellung
Wir hatten bis dato eine sehr gute Auftragslage und leider keine Zeit für eine Homepage. Wir suchen jemaden der uns das Design für die Seite übernimmt und Online stellt. Wir sind auch offen wenn dies über z.B. Q+Z erfolgt. Auf den jeweiligen Seiten wollen wir den Text dann immer selbst eintragen. Seiten: Startseite mit Buttons zu folgenden Feldern: Promotion (Text mit Erklärung was wir machen und Bildern), Personal (Text mit Erklärung was wir machen und Bilder - die Bilder sollten austauschbar sein), Team, Referenzen, Kontaktseite, Gästebuch, Impressum. Die Seite sollte Modern aussehen und nicht zu überladen sein.

```html
<!DOCTYPE html>
<html lang="de">
<head>
<meta charset="utf-8">
<title>Lumo Staffing – Promotion &amp; HR Services</title>
<link rel="stylesheet" href="https://fonts.googleapis.com/css2?family=Nunito+Sans:wght@400;600&display=swap">
<style>
  :root {
    --teal: #7ccfda;
    --teal-light: #a1dce3;
    --button: #6cc5d1;
    --nav-dark: #1f3a40;
    --nav-soft: #4b7880;
    --link: #43666e;
    --ink: #111;
    --white: #fff;
    --logo-grey: #7c8a93;
    --rule: #222;
  }
  * { box-sizing: border-box; margin: 0; padding: 0; }
  html, body { width: 1200px; height: 831px; overflow: hidden; }
  body {
    position: relative;
    background: var(--white);
    font-family: "Nunito Sans", sans-serif;
    color: var(--ink);
  }
  .site-header {
    position: absolute; left: 0; top: 0; width: 1200px; height: 86px;
    background: var(--teal);
  }
  .site-header .accent {
    position: absolute; left: 0; top: 0; width: 1200px; height: 86px;
  }
  .brand {
    position: absolute; left: 99px; top: 24px; width: 84px; height: 84px;
    border-radius: 50%; background: var(--white);
    display: flex; align-items: center; justify-content: center; text-align: center;
    font-size: 11px; font-weight: 600; line-height: 1.15; color: var(--logo-grey);
    z-index: 2;
  }
  .utility-links {
    position: absolute; top: 9px; left: 890px;
    display: flex; align-items: center; gap: 8px;
    font-size: 13px; color: var(--link); letter-spacing: .3px;
  }
  .main-nav a, .utility-links a { color: inherit; text-decoration: none; }
  .main-nav a {
    position: absolute; top: 55px; font-size: 16px; font-weight: 600;
    letter-spacing: 1.2px; color: var(--nav-dark);
  }
  .main-nav a.soft { color: var(--nav-soft); font-weight: 400; }
  .service {
    position: absolute; top: 113px; width: 260px;
  }
  .service h2 {
    text-align: center; font-size: 18px; font-weight: 600; letter-spacing: .3px;
  }
  .service .photo {
    width: 194px; height: 194px; border-radius: 50%;
    margin: 15px auto 0;
  }
  .service p {
    font-size: 12.4px; line-height: 15px; text-align: justify;
    width: 250px; position: absolute; left: 4px;
  }
  .service p.first { top: 258px; }
  .service p.second { top: 318px; }
  .more-button {
    position: absolute; top: 367px; left: 69px; width: 119px; height: 24px;
    background: var(--button); color: var(--white);
    font-size: 13px; font-weight: 600; letter-spacing: .3px;
    display: flex; align-items: center; justify-content: center; gap: 4px;
  }
  .divider {
    position: absolute; left: 129px; top: 592px; width: 942px; height: 1px;
    background: var(--rule);
  }
  .intro h1 {
    position: absolute; left: 131px; top: 666px;
    font-size: 28px; font-weight: 400; letter-spacing: .2px;
  }
  .intro p {
    position: absolute; left: 129px; top: 736px; font-size: 12.4px;
  }
  .intro .photo {
    position: absolute; left: 710px; top: 663px; width: 356px; height: 168px;
    background: linear-gradient(90deg, #e7e9ea 0%, #d6d9da 55%, #6f7b80 78%, #8b969a 100%);
  }
</style>
</head>
<body>
  <header class="site-header">
    <svg class="accent" viewBox="0 0 1200 86" aria-hidden="true">
      <polygon points="775,0 1200,0 1200,86 810,86" fill="var(--teal-light)"/>
    </svg>
    <div class="brand">Lumo<br>Staffing</div>
    <nav class="utility-links">
      <a href="#">Kontakt</a><span>|</span><a href="#">Impressum</a><span>|</span>
      <svg width="13" height="13" viewBox="0 0 13 13" aria-label="Suche"><circle cx="5.5" cy="5.5" r="4.2" fill="none" stroke="currentColor" stroke-width="1.8"/><line x1="8.6" y1="8.6" x2="12" y2="12" stroke="currentColor" stroke-width="2"/></svg>
    </nav>
    <nav class="main-nav">
      <a href="#" style="left:248px">STARTSEITE</a>
      <a href="#" style="left:409px">PROMOTION</a>
      <a href="#" style="left:570px">PERSONAL</a>
      <a href="#" style="left:711px">TEAM</a>
      <a href="#" class="soft" style="left:813px">REFERENZEN</a>
      <a href="#" class="soft" style="left:971px">GÄSTEBUCH</a>
    </nav>
  </header>

  <section class="service" style="left:144px">
    <h2>PROMOTION</h2>
    <div class="photo" role="img" aria-label="Promoterin verteilt Flyer vor einem Gebäude" style="background:radial-gradient(circle at 60% 55%, #c79a72 0%, #7a5a45 40%, #2e2a28 80%)"></div>
    <p class="first">Lorem ipsum dolor sit amet, consectetuer adipiscing elit. Aenean commodo ligula eget dolor.</p>
    <p class="second">Aenean massa. Cum sociis natoque penati­bus et magnis dis parturient montes, nasce-</p>
    <a class="more-button" href="#"><svg width="11" height="11" viewBox="0 0 11 11"><circle cx="5.5" cy="5.5" r="5.5" fill="#fff"/><path d="M3 5.5h4.2M5.3 3.4l2 2.1-2 2.1" stroke="var(--button)" stroke-width="1.5" fill="none"/></svg>MEHR INFOS</a>
  </section>

  <section class="service" style="left:475px">
    <h2>HR-SERVICE</h2>
    <div class="photo" role="img" aria-label="Porträt einer Personalberaterin" style="background:radial-gradient(circle at 50% 45%, #e0bfa3 0%, #b98a62 40%, #6b4a3a 80%)"></div>
    <p class="first">Lorem ipsum dolor sit amet, consectetuer adipiscing elit. Aenean commodo ligula eget dolor.</p>
    <p class="second">Aenean massa. Cum sociis natoque penati­bus et magnis dis parturient montes, nasce-</p>
    <a class="more-button" href="#"><svg width="11" height="11" viewBox="0 0 11 11"><circle cx="5.5" cy="5.5" r="5.5" fill="#fff"/><path d="M3 5.5h4.2M5.3 3.4l2 2.1-2 2.1" stroke="var(--button)" stroke-width="1.5" fill="none"/></svg>MEHR INFOS</a>
  </section>

  <section class="service" style="left:806px">
    <h2>MESSE-HOSTESSEN</h2>
    <div class="photo" role="img" aria-label="Zwei Messe-Hostessen in grauen Blazern" style="background:radial-gradient(circle at 50% 55%, #b9b6b2 0%, #a09a92 45%, #7d7466 85%)"></div>
    <p class="first">Lorem ipsum dolor sit amet, consectetuer adipiscing elit. Aenean commodo ligula eget dolor.</p>
    <p class="second">Aenean massa. Cum sociis natoque penati­bus et magnis dis parturient montes, nasce-</p>
    <a class="more-button" href="#"><svg width="11" height="11" viewBox="0 0 11 11"><circle cx="5.5" cy="5.5" r="5.5" fill="#fff"/><path d="M3 5.5h4.2M5.3 3.4l2 2.1-2 2.1" stroke="var(--button)" stroke-width="1.5" fill="none"/></svg>MEHR INFOS</a>
  </section>

  <div class="divider"></div>

  <section class="intro">
    <h1>International Promotion &amp; HR Services</h1>
    <p>Lorem ipsum dolor sit amet, consectetuer adipiscing elit. Aenean commodo ligula eget</p>
    <div class="photo" role="img" aria-label="Besucher in einer hellen Messehalle"></div>
  </section>
</body>
</html>
```